Business Card for Restaurant Vendal

This project consist of creating 2 design for business card of restaurant named Vendal.

The attached specs below are 'ONLY SUGGESTION' if you have others ideas. You are welcome to post it.

1) Restaurant Card

Adresse:
2784 Côte du Pinard Vert
Montréal (Qc) H4K 3T8

Website:
www.ven-dal.ca

Phone:
438-719-2046

2) Employee Card

Name: Lorna Pik
Title: Owner

Address:
2784 Côte du Pinard Vert
Montréal (Qc) H4K 3T8

Email:lorna@ven-dal.ca
Phone Number:438-719-2046
Cellphone Number:514-830-4162

 The attached specs are 'ONLY SUGGESTION' if you have others ideas.  You are welcome to post it.

Industry/Entity Type

Restaurant

Requirements
Must have
• UV Card Spot

To print Spot UV business cards you would have to submit 2 files for each side. The first file "base" would be your regular design file as it would have been in any other case. The 2nd file "UV mask" is a black/white file. The BLACK color will indicate the areas that will be covered with the UV high gloss finish. To upload the files, please combine front design and front mask file in one P
Nice to have
• 1) The font of the logo should be ink effect
2) black background with wallpaper effect
3) The specs below are 'ONLY SUGGESTION' if you have others ideas. You are welcome to post it.

```html
<!DOCTYPE html>
<html lang="fr">
<head>
<meta charset="utf-8">
<title>Vendal – Employee Card</title>
<link href="https://fonts.googleapis.com/css2?family=Cabin:wght@400;500&family=Roboto+Condensed:wght@700&family=Kalam:wght@700&family=Noto+Sans+JP:wght@700&display=swap" rel="stylesheet">
<style>
  :root {
    --page: #ffffff;
    --ink: #1a1a1a;
    --card-dark: #000000;
    --card-light: #ffffff;
    --card-edge: #c9c9c9;
    --accent: #e63a2b;
    --accent-soft: #f26a4e;
    --paper-text: #ffffff;
  }
  * { box-sizing: border-box; margin: 0; padding: 0; }
  html, body {
    width: 1075px;
    height: 1200px;
    overflow: hidden;
    background: var(--page);
    font-family: "Cabin", sans-serif;
    color: var(--ink);
  }
  .sheet { position: relative; width: 1075px; height: 1200px; }

  .sheet-label {
    position: absolute;
    left: 262px;
    top: 158px;
    font-size: 25px;
    font-weight: 400;
  }

  .card {
    position: absolute;
    left: 255px;
    width: 590px;
    height: 340px;
    border-radius: 42px;
    overflow: hidden;
  }

  /* Front */
  .card-front {
    top: 232px;
    background: var(--card-dark);
    color: var(--paper-text);
  }
  .brand {
    position: absolute;
    left: 72px;
    top: 58px;
    display: flex;
    align-items: center;
    gap: 26px;
  }
  .brand-name {
    font-family: "Roboto Condensed", sans-serif;
    font-weight: 700;
    font-size: 122px;
    line-height: 1;
    letter-spacing: 2px;
    color: var(--paper-text);
  }
  .brand-dot {
    width: 64px;
    height: 64px;
    border-radius: 50%;
    background: var(--accent);
    margin-top: 48px;
  }
  .tagline {
    position: absolute;
    left: 76px;
    top: 228px;
    font-family: "Roboto Condensed", "Noto Sans JP", sans-serif;
    font-weight: 700;
    font-size: 21px;
    letter-spacing: 0.3px;
  }

  /* Back */
  .card-back {
    top: 700px;
    background: var(--card-light);
    border: 2px solid var(--card-edge);
  }
  .person {
    position: absolute;
    left: 38px;
    top: 32px;
  }
  .person-name {
    font-family: "Kalam", cursive;
    font-weight: 700;
    font-size: 31px;
    line-height: 1.1;
  }
  .person-role {
    font-size: 21px;
    margin-top: 2px;
  }
  .contact {
    position: absolute;
    right: 240px;
    top: 136px;
    text-align: right;
    font-size: 21px;
    line-height: 31px;
    list-style: none;
  }
  .contact li { display: flex; justify-content: flex-end; align-items: center; gap: 6px; }
  .contact-badge {
    display: inline-flex;
    align-items: center;
    justify-content: center;
    width: 21px;
    height: 21px;
    border-radius: 50%;
    background: var(--accent);
    color: var(--paper-text);
    font-size: 12px;
    font-weight: 500;
  }
  .address { margin-top: 6px; }
  .address li { display: block; }

  .lantern-art {
    position: absolute;
    left: 430px;
    top: 36px;
    width: 250px;
    height: 290px;
    border-radius: 50%;
    background: radial-gradient(ellipse at 40% 45%, var(--accent-soft), var(--accent) 70%);
  }
</style>
</head>
<body>
  <main class="sheet">
    <p class="sheet-label">Employee Card</p>

    <section class="card card-front" aria-label="Card front">
      <div class="brand">
        <span class="brand-name">Vendal</span>
        <span class="brand-dot"></span>
      </div>
      <p class="tagline">Resto-Bar Japonais · Izakaya · 居酒屋</p>
    </section>

    <section class="card card-back" aria-label="Card back">
      <div class="person">
        <p class="person-name">Lorna Pik</p>
        <p class="person-role">Owner</p>
      </div>
      <ul class="contact">
        <li><span class="contact-badge">E</span>lorna@ven-dal.ca</li>
        <li><span class="contact-badge">T</span>438-719-2046</li>
        <li><span class="contact-badge">M</span>514-830-4162</li>
        <li class="address">
          <ul class="address">
            <li>2784 Côte du Pinard Vert</li>
            <li>Montréal (Qc) H4K 3T8</li>
          </ul>
        </li>
      </ul>
      <div class="lantern-art" role="img" aria-label="Red paper lantern illustration with brushed izakaya characters"></div>
    </section>
  </main>
</body>
</html>
```